The Spoke Loft Cycles Jackson Hole needs a poster for our Snow Tread Days

We need event posters for this week. Here is all of the info:
DAYS OF THE SNOWTREAD
SCHEDULE OF EVENTS:
MONDAY 12/4 6-9pm at The Spoke Loft Cycles
COLD SEASON OPENER- TRAIL GEAR-UP EVENING
Sponsored by Ferncliff Brewing

LIKE BIKES? LIKE FREE BEER? LIKE WINNING STUFF? LIKE DEALS ON GEAR?
Well then we have the perfect night for you!

Come join The Spoke Loft Cycles Crew as the celebrate the beginning of Fat Bike Season!
We are kicking off the winter in the best way possible. How is that you ask? Well by drinking beer and talking bikes with all of you of course. Throw in a free raffle for over $500 worth of gear and it’s an evening that can’t be beat!

Learn about where to ride in Jackson Hole, check out the best new gear and bikes, and meet some new riding buddies all over some cold beverages.

The Spoke Loft Ambassadors and Crew will be hanging out to answer all of your questions about the upcoming Fat Bike Season. Let us get you ready for your best winter bike season yet. We have the expertise to get you into the perfect setup.

Never ridden a Fat Bike? Let us introduce you to your new winter activity. We’ll get you dialed out for the upcoming season with 20% off all Fat Bike related accessories.

This is your chance to get a great deal on all of the Fat Bike gear that you need to shred the groomed this winter. We can’t wait to see you there!
*FREE BEER FROM FERNCLIFF BREWING*
*FREE RAFFLE FOR OVER $500 WORTH OF GEAR*
*20% OFF FAT BIKE ACCESSORIES INCLUDING BOOTS*
*GOOD TIMES AND EVEN BETTER COMPANY*

PLUMP MIDWEEK 12/6 5:30PM at The Spoke Loft Cycles
Group Night Ride & Lolo's After Party

Looking for new friends to ride with? Want to check a new Demo Fat Bike for a great deal? Never been Fat Biking and want to see what it’s all about?

Join Dean Orlov and the rest of The Spoke Loft Crew for a casual first of the season ride up Cache Creek on Fat Bikes. We’re going to go ride the local trails and then enjoy some Margaritas and Cervezas at Lolo’s Taqueria.

We have $10(Usually $60-$80) Demo Fat Bikes and Lights available for this event with reservation. This is an awesome opportunity to ride one of our Tundrax Fat Bikes at a huge discount.

*20% OFF ALL FAT BIKE ACCESSORIES WITH FAT BIKE PURCHASES ALL WEEK*

We need this to be concise and clean. Just include the basic info about each day and the overall discounts.

Target Market(s)

Local Bike Riders. Men 25-50 mainly. Women in the same age group.

Industry/Entity Type

Retail

Colors
33a6d7
ffffff

Requirements
Must have
• Winter Elements. Bike Elements. We are a small bike shop in a small ski town in Wyoming. We are going to use this design for hanging posters around town. This should be a clean design. Must have dates and events.
Nice to have
• Short concise but informative descriptions of each day
Should not have
• Too much text. Details for discounts do not need to be included.

```html
<!DOCTYPE html>
<html lang="en">
<head>
<meta charset="utf-8">
<title>Days of the Snowtread – The Spoke Loft Cycles</title>
<link rel="stylesheet" href="https://fonts.googleapis.com/css2?family=Bungee&family=Saira+Condensed:wght@500;600;700&family=Roboto+Condensed:wght@700&display=swap">
<style>
  :root {
    --sky: #33a6d7;
    --sky-light: #bfeaff;
    --snow: #ffffff;
    --ink: #1c1c1c;
    --bike-grey: #3a3a3a;
    --alert-red: #c3102b;
    --bar: #333333;
  }
  * { margin: 0; padding: 0; box-sizing: border-box; }
  html, body { width: 888px; height: 1200px; overflow: hidden; background: var(--snow); }
  .poster {
    position: relative;
    width: 888px;
    height: 1200px;
    overflow: hidden;
    font-family: "Saira Condensed", "Arial Narrow", sans-serif;
    color: var(--ink);
    background: var(--snow);
  }
  .sky {
    position: absolute; left: 0; top: 0; width: 888px; height: 760px;
    background: radial-gradient(ellipse at 72% 18%, #f2fbff 0%, var(--sky-light) 28%, #6fcdf3 60%, var(--sky) 100%);
  }
  .snowline { position: absolute; left: 0; top: 640px; width: 888px; height: 130px; }
  .shop-name {
    position: absolute; left: 24px; top: 28px; width: 250px;
    font-weight: 700; font-size: 46px; line-height: 0.95; text-transform: uppercase;
    color: var(--ink);
  }
  .shop-name .dot {
    display: inline-block; width: 22px; height: 22px; border-radius: 50%;
    background: var(--sky); margin-left: 6px; vertical-align: middle;
  }
  .title { position: absolute; left: 396px; top: 20px; width: 470px; text-align: center; }
  .title .kicker {
    font-family: "Roboto Condensed", sans-serif; font-weight: 700; font-size: 52px;
    letter-spacing: 3px; color: #2b2b2b; line-height: 1;
  }
  .title .headline {
    font-family: "Bungee", sans-serif; font-size: 56px; line-height: 1.15; color: #111;
    margin-top: 4px;
  }
  .title .dates {
    font-family: "Roboto Condensed", sans-serif; font-weight: 700; font-size: 38px;
    color: var(--alert-red); margin-top: 6px;
  }
  .week-deal {
    position: absolute; left: 512px; top: 252px; width: 370px; text-align: center;
    font-weight: 700; font-size: 38px; line-height: 1.18; text-transform: uppercase; color: #111;
  }
  .bike-art {
    position: absolute; left: 48px; top: 204px; width: 580px; height: 530px;
    border-radius: 48% 48% 20% 20%;
    background: radial-gradient(ellipse at 50% 60%, rgba(58,58,58,0.85) 0%, rgba(58,58,58,0.55) 45%, rgba(58,58,58,0) 72%);
  }
  .event { position: absolute; text-transform: uppercase; }
  .event h2 { font-weight: 700; font-size: 28px; line-height: 1.1; color: #111; }
  .event h3 { font-weight: 600; font-size: 22px; line-height: 1.1; color: #111; }
  .event .when { font-weight: 600; font-size: 22px; color: var(--alert-red); margin: 10px 0 6px; }
  .event ul { list-style: none; }
  .event li { font-weight: 500; font-size: 19px; line-height: 30.5px; }
  .event li::before { content: "* "; font-weight: 700; }
  .event-opener { left: 24px; top: 746px; width: 420px; }
  .event-ride { left: 466px; top: 766px; width: 420px; }
  .event-ride .when { margin-top: 8px; }
  .partner {
    position: absolute; font-weight: 700; text-transform: uppercase; color: #111;
  }
  .partner-brew { left: 56px; top: 1010px; font-size: 24px; }
  .partner-brew .dot {
    display: inline-block; width: 34px; height: 34px; border-radius: 50%;
    background: var(--alert-red); vertical-align: middle; margin-right: 10px;
  }
  .partner-bikes { left: 500px; top: 996px; font-size: 44px; color: #1d5a8c; }
  .info-bar {
    position: absolute; left: 16px; top: 1110px; width: 858px; height: 48px;
    background: var(--bar); color: var(--snow);
    font-weight: 600; font-size: 30px; line-height: 48px; text-align: center; letter-spacing: 1px;
  }
  .info-bar .link { color: #6fd0f6; }
  .footer {
    position: absolute; left: 18px; top: 1164px; width: 856px;
    display: flex; justify-content: space-between;
    font-weight: 600; font-size: 19px; color: var(--alert-red); text-transform: uppercase;
  }
</style>
</head>
<body>
<main class="poster">
  <div class="sky"></div>
  <svg class="snowline" viewBox="0 0 888 130" preserveAspectRatio="none" aria-hidden="true">
    <path d="M0 70 Q120 40 240 64 T480 58 T720 66 T888 52 V130 H0 Z" fill="#ffffff" opacity="0.55"/>
    <path d="M0 96 Q150 74 300 92 T600 88 T888 84 V130 H0 Z" fill="#ffffff"/>
  </svg>
  <div class="bike-art" role="img" aria-label="Silhouette of a fat bike standing in the snow"></div>

  <div class="shop-name">The Spoke Loft<span class="dot"></span><br>Cycles</div>

  <header class="title">
    <div class="kicker">THE DAYS OF THE</div>
    <h1 class="headline">SNOWTREAD</h1>
    <div class="dates">December 4-9, 2017</div>
  </header>

  <p class="week-deal">20% off fat bike<br>accessories with<br>fat bike purchases<br>all week!</p>

  <section class="event event-opener">
    <h2>Cold Season Opener</h2>
    <h3>- Trail Gear-Up Evening</h3>
    <p class="when">Monday, December 4 | 6-9pm</p>
    <ul>
      <li>20% off all fat bike accessories</li>
      <li>Fat bike Q&amp;A</li>
      <li>Free beer from Ferncliff Brewing</li>
      <li>Free raffle for over $500 in gear</li>
    </ul>
  </section>

  <section class="event event-ride">
    <h2>Plump Midweek Group Ride</h2>
    <p class="when">Wednesday, December 6 | 5:30pm</p>
    <ul>
      <li>Meeting at The Spoke Loft Cycles</li>
      <li>$10 fat bike rentals with reservation</li>
      <li>Ride with The Spoke Loft Ambassadors</li>
      <li>After party at Lolo’s Taqueria</li>
    </ul>
  </section>

  <div class="partner partner-brew"><span class="dot"></span>Ferncliff Brewing</div>
  <div class="partner partner-bikes">Tundrax</div>

  <div class="info-bar">VISIT <span class="link">SPOKELOFTCYCLES.COM/EVENTS</span> TO GET MORE INFO</div>

  <footer class="footer">
    <span>The Spoke Loft Cycles | 2740 Timberline Way #3B, Jackson, WY</span>
    <span>Phone: 307.555.0182</span>
  </footer>
</main>
</body>
</html>
```